Inspirational quotes poster shop seeks poster designs

Hi! We are launching an eshop with design posterss featuring inspirational quotes. We need a first poster design while looking for further cooperation on around 20 poster designs. We need outputs in the format that can go to high quality print (size at least 100x70cm).

For the first design feel free to choose any of the following quotes to depict:

1. "Stop starting. Start finishing." Author: Torvald Essunger, Klangora
2. "A problem well stated is a problem half solved." Author: Walter P. Brimsley, American inventor
3. "The best way to predict the future is to invent it." Author: Dale Hubbs, Quince

Designs should be rarther simple, think please of your whole concept and how various posters would go together. Every poster can be quite different though, in terms of fonts, colours and overall design, together they should however form and interesting collage.

Designs must contain the quote, author & company. it can be pure text or some indication of the sense of the quote.

Design must also feature company name/logo (not available yet, for now please use "thoughtvolta" as a working name), QR code with a title "Read the story"

See these posters for design we like (for inspiration ONLY!):
http://www.launchtonics.example/products/launch-print-its-simple-until-you-make-it-complicated
http://www.launchtonics.example/products/launch-print-marcus-feldane-less-meetings-more-doing
http://www.launchtonics.example/products/launch-print-gordon-ashfeld-stop-sketching-start-building

Hi to everybody! Sorry for the spam, some of you have been struggling with finding the crux in the quote, so here I offer some ideas what to look for in them. It's up to you to take it, leave it or change it:)

Stop starting, start finishing -
1 - stop starting with many times repeated small word starting, perhaps large word starting made of small words starting, with it contrasting start finishing in normal bold font.
2 - STARTING could look quite unfinished, sketchy, especially -ING could look more unfinished then the rest , e.g. just rough indication of outline of the letters, again contrasting with start finishing will clean & neat writting.

Problem well stated is a problem half solved - look for something that is clearer by defining the problem. Perhaps in a simple sketch like here http://www.launchtonics.example/products/launch-print-its-simple-until-you-make-it-complicated  point out a route from a problem (light = flame), to a solution (lightbulb, lightbulb design drawing or something like that).

Anyway, despite preference for simple design, I am still looking for some smart, creative, catchy idea in the design. Check with yourself if it's something you can would want to buy and hang up on your wall.

Good luck to all of you and again, thank you all very much for participation!
Radim

Target Market(s)

businesses of every size, from startups to large corporates seeking culture change or motivation kick up

Industry/Entity Type

Shop

Requirements
Must have
• I strongly prefer portrait orientation of the poster!

Nice to have
• Quotes themselves are often on the edge, teasing, so the design can be.
Should not have
• Try to avoid traditional dialoge bubble for the quote itself as the first obvious idea for depicting a quote.

Avoid using photos (not simple then) or too many colours.

Of course, by no means use a COPY of existing designs I linked to for inspiration. It just shows what we like.

```html
<!DOCTYPE html>
<html lang="en">
<head>
<meta charset="utf-8">
<title>Stop Starting. Start Finishing.</title>
<link href="https://fonts.googleapis.com/css2?family=Roboto:wght@400;700;900&display=swap" rel="stylesheet">
<style>
  :root {
    --lime-light: #b4e85a;
    --lime: #9ed944;
    --lime-edge: #86c932;
    --lime-deep: #72b82a;
    --white: #ffffff;
    --ghost: rgba(255, 255, 255, 0.38);
  }
  html, body {
    margin: 0;
    padding: 0;
    width: 900px;
    height: 1200px;
    overflow: hidden;
  }
  .poster {
    position: relative;
    width: 900px;
    height: 1200px;
    overflow: hidden;
    background: radial-gradient(ellipse at 50% 45%, var(--lime-light) 0%, var(--lime) 55%, var(--lime-edge) 100%);
    font-family: "Roboto", Arial, sans-serif;
    color: var(--white);
  }
  .author-tag {
    position: absolute;
    left: 118px;
    top: 112px;
    width: 74px;
    height: 126px;
  }
  .author-tag svg {
    position: absolute;
    inset: 0;
  }
  .author-text {
    position: absolute;
    left: 10px;
    top: 44px;
    margin: 0;
    font-size: 11px;
    line-height: 1.25;
    font-weight: 700;
  }
  .author-text .company {
    display: block;
    margin-top: 12px;
    font-weight: 400;
    opacity: 0.85;
  }
  .headline-stop {
    position: absolute;
    left: 222px;
    top: 124px;
    margin: 0;
    font-size: 180px;
    font-weight: 700;
    line-height: 1;
    letter-spacing: -4px;
  }
  .starting-field {
    position: absolute;
    left: 264px;
    top: 306px;
    width: 380px;
    overflow: hidden;
  }
  .starting-row {
    height: 13.9px;
    overflow: hidden;
    white-space: nowrap;
    font-size: 11.5px;
    font-weight: 700;
    line-height: 13.9px;
    letter-spacing: 0.2px;
  }
  .starting-row .ing { color: var(--ghost); }
  .starting-row:nth-child(3n+2) { text-indent: -30px; }
  .starting-row:nth-child(3n) { text-indent: -58px; }
  .starting-row.short { width: 345px; }
  .full-stop {
    position: absolute;
    left: 621px;
    top: 600px;
    width: 30px;
    height: 30px;
    background: var(--white);
  }
  .headline-start {
    position: absolute;
    left: 172px;
    top: 736px;
    margin: 0;
    font-size: 180px;
    font-weight: 700;
    line-height: 1;
    letter-spacing: -2px;
  }
  .headline-finishing {
    position: absolute;
    left: 174px;
    top: 884px;
    margin: 0;
    font-size: 120px;
    font-weight: 700;
    line-height: 1;
    letter-spacing: -1px;
  }
  .finish-arrow {
    position: absolute;
    left: 740px;
    top: 918px;
  }
  .brand {
    position: absolute;
    left: 0;
    right: 0;
    top: 1096px;
    display: flex;
    justify-content: center;
    align-items: center;
    gap: 6px;
    font-size: 17px;
    font-weight: 700;
  }
  .brand-dot {
    width: 20px;
    height: 20px;
    border-radius: 50%;
    background: var(--lime-deep);
  }
  .story-link {
    position: absolute;
    left: 0;
    right: 0;
    top: 1130px;
    display: flex;
    flex-direction: column;
    align-items: center;
    gap: 4px;
  }
  .qr-slot {
    width: 34px;
    height: 34px;
    background: var(--lime-deep);
  }
  .story-title {
    font-size: 9px;
    font-weight: 400;
    letter-spacing: 0.3px;
    opacity: 0.85;
  }
</style>
</head>
<body>
<main class="poster">
  <aside class="author-tag">
    <svg width="74" height="126" viewBox="0 0 74 126" aria-hidden="true">
      <path d="M0 0 L16 0 L16 14 L66 14 Q74 14 74 22 L74 118 Q74 126 66 126 L8 126 Q0 126 0 118 Z" fill="var(--lime-deep)"/>
    </svg>
    <p class="author-text">Torvald<br>Essunger<span class="company">Klangora</span></p>
  </aside>

  <h1 class="headline-stop">STOP</h1>

  <div class="starting-field" aria-label="starting, repeated">
    <div class="starting-row">START<span class="ing">ING</span> START<span class="ing">ING</span> START<span class="ing">ING</span> START<span class="ing">ING</span> START<span class="ing">ING</span> START<span class="ing">ING</span></div>
    <div class="starting-row">START<span class="ing">ING</span> START<span class="ing">ING</span> START<span class="ing">ING</span> START<span class="ing">ING</span> START<span class="ing">ING</span> START<span class="ing">ING</span></div>
    <div class="starting-row">START<span class="ing">ING</span> START<span class="ing">ING</span> START<span class="ing">ING</span> START<span class="ing">ING</span> START<span class="ing">ING</span> START<span class="ing">ING</span></div>
    <div class="starting-row">START<span class="ing">ING</span> START<span class="ing">ING</span> START<span class="ing">ING</span> START<span class="ing">ING</span> START<span class="ing">ING</span> START<span class="ing">ING</span></div>
    <div class="starting-row">START<span class="ing">ING</span> START<span class="ing">ING</span> START<span class="ing">ING</span> START<span class="ing">ING</span> START<span class="ing">ING</span> START<span class="ing">ING</span></div>
    <div class="starting-row">START<span class="ing">ING</span> START<span class="ing">ING</span> START<span class="ing">ING</span> START<span class="ing">ING</span> START<span class="ing">ING</span> START<span class="ing">ING</span></div>
    <div class="starting-row">START<span class="ing">ING</span> START<span class="ing">ING</span> START<span class="ing">ING</span> START<span class="ing">ING</span> START<span class="ing">ING</span> START<span class="ing">ING</span></div>
    <div class="starting-row">START<span class="ing">ING</span> START<span class="ing">ING</span> START<span class="ing">ING</span> START<span class="ing">ING</span> START<span class="ing">ING</span> START<span class="ing">ING</span></div>
    <div class="starting-row">START<span class="ing">ING</span> START<span class="ing">ING</span> START<span class="ing">ING</span> START<span class="ing">ING</span> START<span class="ing">ING</span> START<span class="ing">ING</span></div>
    <div class="starting-row">START<span class="ing">ING</span> START<span class="ing">ING</span> START<span class="ing">ING</span> START<span class="ing">ING</span> START<span class="ing">ING</span> START<span class="ing">ING</span></div>
    <div class="starting-row">START<span class="ing">ING</span> START<span class="ing">ING</span> START<span class="ing">ING</span> START<span class="ing">ING</span> START<span class="ing">ING</span> START<span class="ing">ING</span></div>
    <div class="starting-row">START<span class="ing">ING</span> START<span class="ing">ING</span> START<span class="ing">ING</span> START<span class="ing">ING</span> START<span class="ing">ING</span> START<span class="ing">ING</span></div>
    <div class="starting-row">START<span class="ing">ING</span> START<span class="ing">ING</span> START<span class="ing">ING</span> START<span class="ing">ING</span> START<span class="ing">ING</span> START<span class="ing">ING</span></div>
    <div class="starting-row">START<span class="ing">ING</span> START<span class="ing">ING</span> START<span class="ing">ING</span> START<span class="ing">ING</span> START<span class="ing">ING</span> START<span class="ing">ING</span></div>
    <div class="starting-row">START<span class="ing">ING</span> START<span class="ing">ING</span> START<span class="ing">ING</span> START<span class="ing">ING</span> START<span class="ing">ING</span> START<span class="ing">ING</span></div>
    <div class="starting-row">START<span class="ing">ING</span> START<span class="ing">ING</span> START<span class="ing">ING</span> START<span class="ing">ING</span> START<span class="ing">ING</span> START<span class="ing">ING</span></div>
    <div class="starting-row">START<span class="ing">ING</span> START<span class="ing">ING</span> START<span class="ing">ING</span> START<span class="ing">ING</span> START<span class="ing">ING</span> START<span class="ing">ING</span></div>
    <div class="starting-row">START<span class="ing">ING</span> START<span class="ing">ING</span> START<span class="ing">ING</span> START<span class="ing">ING</span> START<span class="ing">ING</span> START<span class="ing">ING</span></div>
    <div class="starting-row">START<span class="ing">ING</span> START<span class="ing">ING</span> START<span class="ing">ING</span> START<span class="ing">ING</span> START<span class="ing">ING</span> START<span class="ing">ING</span></div>
    <div class="starting-row">START<span class="ing">ING</span> START<span class="ing">ING</span> START<span class="ing">ING</span> START<span class="ing">ING</span> START<span class="ing">ING</span> START<span class="ing">ING</span></div>
    <div class="starting-row">START<span class="ing">ING</span> START<span class="ing">ING</span> START<span class="ing">ING</span> START<span class="ing">ING</span> START<span class="ing">ING</span> START<span class="ing">ING</span></div>
    <div class="starting-row short">START<span class="ing">ING</span> START<span class="ing">ING</span> START<span class="ing">ING</span> START<span class="ing">ING</span> START<span class="ing">ING</span> START<span class="ing">ING</span></div>
    <div class="starting-row short">START<span class="ing">ING</span> START<span class="ing">ING</span> START<span class="ing">ING</span> START<span class="ing">ING</span> START<span class="ing">ING</span> START<span class="ing">ING</span></div>
    <div class="starting-row short">START<span class="ing">ING</span> START<span class="ing">ING</span> START<span class="ing">ING</span> START<span class="ing">ING</span> START<span class="ing">ING</span> START<span class="ing">ING</span></div>
  </div>
  <div class="full-stop" aria-hidden="true"></div>

  <h2 class="headline-start">START</h2>
  <h2 class="headline-finishing">FINISHING</h2>
  <svg class="finish-arrow" width="32" height="56" viewBox="0 0 32 56" aria-hidden="true">
    <polygon points="0,0 32,28 0,56" fill="var(--white)"/>
  </svg>

  <footer class="brand">
    <span class="brand-dot" aria-hidden="true"></span>
    <span class="brand-name">thoughtvolta</span>
  </footer>
  <div class="story-link">
    <div class="qr-slot" role="img" aria-label="QR code linking to the story behind the quote"></div>
    <span class="story-title">Read the story</span>
  </div>
</main>
</body>
</html>
```